Budget Brand Responsive Website

Flat vector style website needed for value based IT support company. looking for clean, illustration intensive based design. Current test site can be found at www.bolt-pc.co.uk and holding page it www.boltpc.co.uk this will show text and services, please feel free to use placeholder text if you think we need alternative text in places. Emphasis should be on low cost support and services listed on the site, would be nice to see costs in bold images. important colors are the blue, orange and white, see holding page and attached image of an advert

Industry/Entity Type

It Company

Coding

Coded - Design and coding required

```html
<!DOCTYPE html>
<html lang="en">
<head>
<meta charset="utf-8">
<title>Bolt PC – IT Services</title>
<link href="https://fonts.googleapis.com/css2?family=Open+Sans:wght@400;600;700;800&display=swap" rel="stylesheet">
<style>
:root{
  --blue:#3d84d6;
  --blue-light:#5a9ae2;
  --blue-pale:#dbe8f7;
  --navy:#1f4a86;
  --orange:#f07f1e;
  --orange-dark:#d96c10;
  --red:#d9342b;
  --ink:#222;
  --grey:#555;
  --white:#fff;
}
*{margin:0;padding:0;box-sizing:border-box}
html,body{width:1200px;height:4286px;overflow:hidden}
body{position:relative;background:var(--white);font-family:"Open Sans",Arial,sans-serif;color:var(--ink)}
.band{position:absolute;left:0;width:1200px}
.abs{position:absolute}

/* header + hero */
.hero-band{top:0;height:660px;background:var(--blue);clip-path:polygon(0 0,100% 0,100% 88%,0 100%)}
.brand{left:60px;top:40px;display:flex;align-items:center;gap:14px;color:var(--white);font-weight:800;font-size:44px;letter-spacing:1px}
.brand-square{width:40px;height:40px;background:var(--white)}
.nav{right:60px;top:58px;display:flex;gap:26px;font-size:17px;color:var(--white)}
.nav a{color:inherit;text-decoration:none;padding:4px 8px}
.nav a.active{background:var(--orange)}
.hero-art{left:150px;top:120px;width:900px;height:370px;border-radius:8px;background:radial-gradient(circle at 50% 45%,#f4f7fb 0,#cfe0f3 45%,var(--blue-light) 100%)}
.hero-title{left:60px;top:505px;color:var(--white);font-weight:800;font-size:50px;letter-spacing:1px;line-height:1.1}
.hero-sub{left:60px;top:566px;color:var(--white);font-weight:700;font-size:19px}

/* stats */
.stats{left:60px;top:730px;width:1080px;display:flex;justify-content:space-between}
.stat{width:330px;text-align:center}
.stat-num{font-size:44px;font-weight:700;line-height:1}
.stat-label{font-size:24px;margin-top:4px}
.stat p{font-size:12.5px;color:var(--grey);text-align:left;margin-top:18px;line-height:1.45}
.people{left:0;top:900px;width:1200px;height:240px;background:linear-gradient(180deg,rgba(61,132,214,0) 0,rgba(61,132,214,.35) 60%,rgba(61,132,214,.6) 100%)}

/* tied down */
.tied-band{top:1130px;height:300px;background:var(--blue);clip-path:polygon(0 10%,100% 0,100% 90%,0 100%)}
.tied-title{left:0;top:1175px;width:1200px;text-align:center;color:var(--red);font-size:26px;font-weight:700;text-decoration:underline}
.tied-text{left:100px;top:1230px;width:1000px;color:var(--white);font-size:13px;line-height:1.5}
.tied-text p+p{margin-top:12px}
.tied-call{left:0;top:1322px;width:1200px;text-align:center;color:var(--white);font-size:30px;font-weight:700}

/* section headings */
.section-title{left:0;width:1200px;text-align:center;color:var(--red);font-size:26px;font-weight:700;text-decoration:underline}

/* services */
.services-band{top:1620px;height:860px;background:var(--blue-pale);clip-path:polygon(0 6%,100% 0,100% 94%,0 100%)}
.services{left:90px;top:1565px;width:1020px;display:grid;grid-template-columns:repeat(3,320px);column-gap:30px;row-gap:20px}
.service{height:470px;background:var(--orange);border-radius:6px;text-align:center;color:var(--white);padding:34px 26px;box-shadow:0 4px 0 var(--orange-dark)}
.service:nth-child(n+4){height:385px;padding-top:28px}
.service-icon{width:150px;height:150px;border-radius:50%;margin:0 auto;background:radial-gradient(circle,#fff 0,#bcd6f2 55%,var(--blue) 100%);border:6px solid var(--white)}
.service h3{font-size:30px;font-weight:700;margin:16px 0 16px}
.service ul{list-style:none;font-size:13px;line-height:1.7}
.more{display:inline-block;background:var(--white);color:var(--orange);font-size:14px;font-weight:600;padding:8px 44px;border-radius:3px;margin-top:22px}

/* pricing */
.pricing-band{top:2480px;height:420px;background:var(--blue);clip-path:polygon(0 8%,100% 0,100% 92%,0 100%)}
.pricing-title{color:var(--white)}
.pricing{left:90px;top:2593px;width:1020px;display:flex;justify-content:space-between}
.price-card{width:238px;height:257px;background:var(--orange);color:var(--white);padding:18px 16px;text-align:center;border-radius:4px}
.price-card h3{font-size:28px;font-weight:800}
.price-card .tag{font-size:12px;font-weight:700;margin:4px 0 16px}
.price-card ul{list-style:none;font-size:12px;line-height:1.75;text-align:left}
.price-card .more{margin-top:18px}

/* tech support */
.tech-text{left:100px;top:2995px;width:1000px;font-size:13px;color:var(--grey);line-height:1.5}
.tech-text p+p{margin-top:10px}

/* about */
.about-band{top:3130px;height:320px;background:var(--blue);clip-path:polygon(0 0,100% 12%,100% 100%,0 88%)}
.about-title{color:var(--white)}
.about-text{left:100px;top:3285px;width:1000px;color:var(--white);font-size:12.5px;line-height:1.5}
.about-text p+p{margin-top:8px}

/* contact */
.contact-info{left:240px;top:3610px;width:440px;display:grid;grid-template-columns:1fr 1fr;row-gap:28px;column-gap:30px;font-size:12.5px;line-height:1.55}
.contact-info h4{font-size:13px;font-weight:700}
.contact-form{left:690px;top:3610px;width:340px}
.field{border:1px solid #aac7ea;height:44px;margin-bottom:14px;font-size:12px;color:#888;padding:12px}
.field.message{height:150px}
.submit{display:block;margin-left:auto;width:80px;background:var(--blue);color:var(--white);text-align:center;font-size:13px;padding:8px 0}

/* footer */
.footer-band{top:3980px;height:306px;background:var(--blue);clip-path:polygon(0 18%,100% 0,100% 100%,0 100%)}
.footer-cols{left:100px;top:4085px;width:1000px;display:flex;justify-content:space-between;align-items:flex-start;color:var(--white);font-size:12.5px}
.footer-col h5{font-size:14px;margin-bottom:8px}
.footer-col ul{list-style:none;line-height:1.6}
.footer-pair{display:flex;gap:40px}
.footer-brand{display:flex;align-items:center;gap:12px;font-size:48px;font-weight:800;color:var(--white);margin-top:20px}
.footer-brand span.sq{width:40px;height:40px;background:var(--white)}
.social{display:flex;flex-direction:column;gap:6px}
.social li{display:flex;align-items:center;gap:8px}
.social .dot{width:16px;height:16px;border-radius:50%;background:var(--white)}
.copyright{left:0;top:4240px;width:1200px;height:46px;background:var(--navy);color:var(--white);font-size:12px;text-align:center;line-height:46px}
</style>
</head>
<body>

<div class="band hero-band"></div>
<div class="abs brand"><span class="brand-square"></span>BOLT PC</div>
<nav class="abs nav"><a class="active">Home</a><a>Support</a><a>Services</a><a>About</a><a>Contact</a></nav>
<div class="abs hero-art" role="img" aria-label="Flat illustration of a businessman surrounded by charts, a calendar, a clock, a question mark and a lightbulb"></div>
<h1 class="abs hero-title">IT SERVICES THE SIMPLE WAY</h1>
<div class="abs hero-sub">WE HELP OUR CLIENTS INCREASE PRODUCTIVITY WHILST REDUCING COST</div>

<section class="abs stats">
  <div class="stat"><div class="stat-num">678</div><div class="stat-label">Awesome Projects</div>
    <p>Bolt PC has delivered hundreds of projects for small firms across the region, from network upgrades to full office moves, always on time and always within a budget agreed before any work begins.</p></div>
  <div class="stat"><div class="stat-num">11 123</div><div class="stat-label">Happy Customers</div>
    <p>Our customers stay because support is simple. One phone number, friendly engineers and a clear monthly price mean problems are solved quickly and your team can get back to the work that matters.</p></div>
  <div class="stat"><div class="stat-num">234</div><div class="stat-label">Professional Awards</div>
    <p>Industry recognition for service quality and value has followed us year after year, and we are proud that every award reflects the trust our local business community places in our team.</p></div>
</section>
<div class="abs people" role="img" aria-label="Row of business people silhouettes in soft blue"></div>

<div class="band tied-band"></div>
<h2 class="abs tied-title">DON'T GET TIED DOWN!</h2>
<div class="abs tied-text">
  <p>No long contracts and no hidden fees. Choose the support you need each month and scale up or down whenever your business changes. Our plans are built to keep costs low while giving you fast, reliable help.</p>
  <p>Switching to Bolt PC is easy and we handle the move for you.</p>
</div>
<div class="abs tied-call">Call us today on 01632 960 418</div>

<h2 class="abs section-title" style="top:1508px">SERVICES TAILORED FOR YOU</h2>
<div class="band services-band"></div>
<section class="abs services">
  <article class="service"><div class="service-icon" role="img" aria-label="Support icon illustration"></div><h3>SUPPORT</h3><ul><li>Unlimited Remote Support</li><li>Fixed Monthly Price Per User</li><li>On-Site Visits Available</li></ul><span class="more">More</span></article>
  <article class="service"><div class="service-icon" role="img" aria-label="Voice icon illustration"></div><h3>VOICE</h3><ul><li>Low Cost Business Calls</li><li>Free Number Porting</li><li>Desk And Mobile Handsets</li></ul><span class="more">More</span></article>
  <article class="service"><div class="service-icon" role="img" aria-label="Internet icon illustration"></div><h3>INTERNET</h3><ul><li>Business Fibre Broadband</li><li>Static IP Included</li><li>Next Day Fault Repair</li></ul><span class="more">More</span></article>
  <article class="service"><div class="service-icon" role="img" aria-label="Security icon illustration"></div><h3>SECURITY</h3><ul><li>Managed Antivirus</li><li>Firewall And Backup</li></ul><span class="more">More</span></article>
  <article class="service"><div class="service-icon" role="img" aria-label="Hosting icon illustration"></div><h3>HOSTING</h3><ul><li>Website And Email Hosting</li><li>Domain Registration</li></ul><span class="more">More</span></article>
  <article class="service"><div class="service-icon" role="img" aria-label="Cloud icon illustration"></div><h3>CLOUD</h3><ul><li>Office Apps In The Cloud</li><li>Secure File Sharing</li></ul><span class="more">More</span></article>
</section>

<div class="band pricing-band"></div>
<h2 class="abs section-title pricing-title" style="top:2532px">PRICING FOR OUR MOST POPULAR SERVICES</h2>
<section class="abs pricing">
  <article class="price-card"><h3>SUPPORT</h3><div class="tag">From £15 Per User Monthly</div><ul><li>Remote Help Desk</li><li>Patch Management</li><li>Monthly Health Report</li></ul><span class="more">More</span></article>
  <article class="price-card"><h3>VOICE</h3><div class="tag">From £8 Per Line Monthly</div><ul><li>Free UK Landline Calls</li><li>Voicemail To Email</li><li>Call Recording Option</li></ul><span class="more">More</span></article>
  <article class="price-card"><h3>HOSTING</h3><div class="tag">From £5 Per Site Monthly</div><ul><li>Fast SSD Servers</li><li>Daily Site Backups</li><li>Free SSL Certificate</li></ul><span class="more">More</span></article>
  <article class="price-card"><h3>CLOUD</h3><div class="tag">From £6 Per User Monthly</div><ul><li>Hosted Email</li><li>Online File Storage</li><li>Virtual Desktops</li></ul><span class="more">More</span></article>
</section>

<h2 class="abs section-title" style="top:2942px;color:var(--ink)">TECHNICAL SUPPORT</h2>
<div class="abs tech-text">
  <p>Our help desk is staffed by qualified engineers who answer calls promptly and resolve most issues remotely within minutes. Where a visit is needed we send a local engineer the same or next working day.</p>
  <p>Every plan includes monitoring, updates and a named account contact, so you always know who to call.</p>
</div>

<div class="band about-band"></div>
<h2 class="abs section-title about-title" style="top:3232px">ABOUT BOLT PC</h2>
<div class="abs about-text">
  <p>Bolt PC was founded to give small businesses the same quality of IT support enjoyed by large companies, at a price that makes sense. We are a local team with years of experience across networks, telephony and cloud services.</p>
  <p>We believe in plain language, honest pricing and long relationships built on results. Whether you have two staff or two hundred, we will design a service around the way you work and keep it running smoothly.</p>
  <p>Get in touch to arrange a free review of your current setup.</p>
</div>

<h2 class="abs section-title" style="top:3522px;color:var(--ink)">CONTACT US</h2>
<div class="abs contact-info">
  <div><h4>Head Office</h4>12 Harbour Road<br>Westmere<br>WM1 4TQ</div>
  <div><h4>Support</h4>help@boltpc.co.uk<br>Tel: 01632 960 418</div>
  <div><h4>Kelbrook Office</h4>7 Mill Lane<br>Kelbrook<br>KB2 8RD</div>
  <div><h4>Sales</h4>sales@boltpc.co.uk<br>Tel: 01632 960 419</div>
</div>
<form class="abs contact-form">
  <div class="field">Name</div>
  <div class="field">Email</div>
  <div class="field message">Type your message</div>
  <span class="submit">More</span>
</form>

<div class="band footer-band"></div>
<footer class="abs footer-cols">
  <div class="footer-pair">
    <div class="footer-col"><h5>Quicklinks</h5><ul><li>Home</li><li>Support</li><li>Services</li><li>About</li><li>Contact</li></ul></div>
    <div class="footer-col"><h5>Services</h5><ul><li>Voice</li><li>Internet</li><li>Security</li><li>Hosting</li><li>Cloud</li></ul></div>
  </div>
  <div class="footer-brand"><span class="sq"></span>BOLT PC</div>
  <div class="footer-pair">
    <div class="footer-col"><h5>Support</h5><ul><li>IT Support</li><li>Remote Help</li><li>On-Site Visits</li><li>Pricing</li></ul></div>
    <div class="footer-col"><h5>About</h5><ul class="social"><li><span class="dot"></span>Follow</li><li><span class="dot"></span>Like</li><li><span class="dot"></span>Connect</li><li><span class="dot"></span>Share</li></ul></div>
  </div>
</footer>
<div class="abs copyright">© 2015 Bolt PC Ltd · Registered in England · All rights reserved</div>

</body>
</html>
```